Letterhead and Stationary for Construction Company

Lumen Forge needs modern Letterhead, Envelopes and Notepad designs.

Industry/Entity Type

Construction

Colors
f78f20
34a7d8
ffffff

Requirements
Must have
• Modern looking design.

```html
<!DOCTYPE html>
<html lang="en">
<head>
<meta charset="utf-8">
<title>Lumen Forge Stationery</title>
<link href="https://fonts.googleapis.com/css2?family=Open+Sans:wght@400;600;700&display=swap" rel="stylesheet">
<style>
  :root {
    --orange: #f26a22;
    --orange-light: #f58f4f;
    --blue: #1b5ea6;
    --white: #ffffff;
    --ink: #4a4a4a;
    --backdrop: #f3c29f;
    --backdrop-edge: #c9987a;
  }
  * { box-sizing: border-box; margin: 0; padding: 0; }
  html, body { width: 1200px; height: 803px; overflow: hidden; }
  body {
    font-family: "Open Sans", Arial, sans-serif;
    background: radial-gradient(ellipse at center, var(--backdrop) 55%, var(--backdrop-edge) 100%);
    position: relative;
  }
  .sheet { position: absolute; background: var(--white); box-shadow: 0 4px 14px rgba(90,50,20,.25); overflow: hidden; }

  .brand { display: flex; align-items: center; gap: 6px; font-weight: 600; color: var(--orange); letter-spacing: .2px; white-space: nowrap; }
  .brand-dot { width: .7em; height: .7em; border-radius: 50%; background: var(--orange); flex: none; }
  .brand.on-orange { color: var(--white); }
  .brand.on-orange .brand-dot { background: var(--white); }

  /* Business card front */
  .card-front { left: 60px; top: 250px; width: 210px; height: 120px;
    background: linear-gradient(160deg, var(--orange-light), var(--orange) 70%); }
  .card-front .brand { position: absolute; left: 50%; top: 40px; transform: translateX(-50%); font-size: 20px; }
  .card-front .web-tab { position: absolute; right: 26px; bottom: 6px; background: var(--blue); color: var(--white);
    font-size: 8px; font-weight: 600; padding: 3px 10px; }
  .card-front .base-line { position: absolute; left: 0; right: 0; bottom: 0; height: 6px; background: var(--blue); }

  /* Business card back */
  .card-back { left: 300px; top: 170px; width: 210px; height: 120px; }
  .card-back .brand { position: absolute; left: 12px; top: 50px; font-size: 13px; gap: 5px; }
  .card-back .divider { position: absolute; left: 116px; top: 20px; width: 1px; height: 56px; background: #bbb; }
  .card-back .details { position: absolute; left: 122px; top: 20px; list-style: none; font-size: 5.5px; color: var(--ink); line-height: 9px; white-space: nowrap; }
  .card-back .details li::before { content: "•"; color: var(--blue); margin-right: 3px; }
  .card-back .stripe-o { position: absolute; left: 0; bottom: 6px; width: 150px; height: 3px; background: var(--orange); }
  .card-back .stripe-b { position: absolute; right: 0; bottom: 8px; width: 50px; height: 3px; background: var(--blue); }

  /* Envelope */
  .envelope { left: 60px; top: 400px; width: 440px; height: 200px; background: var(--orange); position: absolute;
    box-shadow: 0 4px 14px rgba(90,50,20,.3); }
  .envelope svg { position: absolute; inset: 0; }

  /* Letterhead */
  .letterhead { left: 790px; top: 60px; width: 360px; height: 510px; }
  .letterhead .rule-blue { position: absolute; right: 0; top: 36px; width: 110px; height: 4px; background: var(--blue); }
  .letterhead .rule-orange { position: absolute; left: 0; top: 58px; width: 120px; height: 4px; background: var(--orange); }
  .letterhead .brand { position: absolute; left: 50%; top: 34px; transform: translateX(-50%); font-size: 20px; }

  .footer { position: absolute; left: 0; right: 0; bottom: 0; }
  .footer .web-band { position: absolute; right: 0; bottom: 10px; background: var(--blue); color: var(--white);
    font-size: 10px; font-weight: 600; padding: 5px 10px; white-space: nowrap; }
  .footer .contact { position: absolute; left: 12px; right: 142px; bottom: 16px; display: flex; flex-wrap: wrap;
    column-gap: 8px; row-gap: 2px; font-size: 6px; line-height: 8px; color: var(--ink); white-space: nowrap; }
  .footer .contact span::before { content: "●"; color: var(--blue); margin-right: 3px; font-size: 5px; }
  .footer .base { position: absolute; left: 0; right: 0; bottom: 0; height: 10px;
    background: linear-gradient(var(--orange) 0 3px, transparent 3px 5px, var(--blue) 5px); }

  .notepad { left: 300px; top: 560px; width: 470px; height: 210px; }
  .notepad .rule-orange { position: absolute; left: 0; top: 44px; width: 26px; height: 3px; background: var(--orange); }
  .notepad .rule-blue { position: absolute; left: 150px; right: 0; top: 44px; height: 3px; background: var(--blue); }
  .notepad .brand { position: absolute; left: 32px; top: 34px; font-size: 17px; }
  .notepad .footer .contact { column-gap: 7px; }
</style>
</head>
<body>

  <div class="sheet card-front">
    <div class="brand on-orange"><span class="brand-dot"></span>lumenforge</div>
    <div class="web-tab">www.lumenforge.com</div>
    <div class="base-line"></div>
  </div>

  <div class="sheet card-back">
    <div class="brand"><span class="brand-dot"></span>lumenforge</div>
    <div class="divider"></div>
    <ul class="details">
      <li>00 Harbour Rd. Kestwick</li>
      <li>Valeshire KV0 0LF</li>
      <li>T: 00 000 000000</li>
      <li>F: 00 000 000000</li>
      <li>contact@lumenforge.com</li>
      <li>www.lumenforge.com</li>
    </ul>
    <div class="stripe-o"></div>
    <div class="stripe-b"></div>
  </div>

  <div class="envelope">
    <svg width="440" height="200" viewBox="0 0 440 200">
      <polyline points="0,0 250,120 440,0" fill="none" stroke="#c9541a" stroke-width="1.5"/>
    </svg>
  </div>

  <div class="sheet notepad">
    <div class="rule-orange"></div>
    <div class="brand"><span class="brand-dot"></span>lumenforge</div>
    <div class="rule-blue"></div>
    <div class="footer">
      <div class="contact">
        <span>00 Harbour Rd. Kestwick Valeshire KV 00 0LF</span>
        <span>(00000) 000003</span>
        <span>(00000) 000003</span>
        <span>contact@lumenforge.com</span>
      </div>
      <div class="web-band">www.lumenforge.com</div>
      <div class="base"></div>
    </div>
  </div>

  <div class="sheet letterhead">
    <div class="rule-blue"></div>
    <div class="brand"><span class="brand-dot"></span>lumenforge</div>
    <div class="rule-orange"></div>
    <div class="footer">
      <div class="contact">
        <span>00 Harbour Rd. Kestwick Valeshire KV 00 0LF</span>
        <span>(00000) 000003</span>
        <span>(00000) 000003</span>
        <span>contact@lumenforge.com</span>
      </div>
      <div class="web-band">www.lumenforge.com</div>
      <div class="base"></div>
    </div>
  </div>

</body>
</html>
```